Marlow Label design search/01

We need a label design for a new customers chemical products. The label is 275mm wide and 165mm high. The design will be simple with lots of space left for us to thermally print the information required on each label. This thermal print is black. From the top down 70mm the label will be white. The logo size will be about 50mm-55mm across and 40mm-45mm down. The logo position needs to be 1 of the following positions
a) Cetred at the bottom
b) Centred at the top
c) At the bottom no closer than 70mm to the right edge
The attached logo has 8 logos on it and we would like the Marlow Reagents on the left.
Requirements
Must have
- Logo
- look at attached info
Nice to have
- Simple and clean

```html
<!DOCTYPE html>
<html lang="en">
<head>
<meta charset="utf-8">
<title>Marlow Reagents – Product Label</title>
<link rel="stylesheet" href="https://fonts.googleapis.com/css2?family=Exo+2:wght@700&display=swap">
<style>
  :root {
    --backdrop: #e4e4e4;
    --label-white: #ffffff;
    --brand-red: #b3180e;
    --brand-red-soft: #dc958f;
    --brand-red-faint: #f6e2e0;
  }
  * { margin: 0; padding: 0; box-sizing: border-box; }
  html, body {
    width: 1200px;
    height: 909px;
    overflow: hidden;
    background: var(--backdrop);
  }
  .canvas {
    position: relative;
    width: 1200px;
    height: 909px;
  }
  .label {
    position: absolute;
    left: 50px;
    top: 124px;
    width: 1100px;
    height: 660px;
    background: var(--label-white);
    overflow: hidden;
  }
  .brand-lockup {
    position: absolute;
    top: 48px;
    left: 0;
    width: 100%;
    text-align: center;
    font-family: "Exo 2", sans-serif;
    font-weight: 700;
    color: var(--brand-red);
    line-height: 1;
  }
  .brand-name {
    display: block;
    font-size: 58px;
    letter-spacing: 3px;
    text-transform: uppercase;
  }
  .brand-descriptor {
    display: block;
    margin-top: 14px;
    font-size: 18px;
    letter-spacing: 1px;
    text-transform: uppercase;
  }
  .pattern-field {
    position: absolute;
    left: 0;
    right: 0;
    top: 248px;
    bottom: 0;
    background: linear-gradient(
      to bottom,
      var(--label-white) 0%,
      var(--brand-red-faint) 12%,
      var(--brand-red-soft) 55%,
      var(--brand-red) 100%
    );
  }
</style>
</head>
<body>
  <div class="canvas">
    <section class="label">
      <div class="brand-lockup">
        <span class="brand-name">Marlow</span>
        <span class="brand-descriptor">Reagents</span>
      </div>
      <div class="pattern-field" role="img" aria-label="Repeating interlocking curved-loop pattern in red, fading to white toward the top"></div>
    </section>
  </div>
</body>
</html>
```